Mesa Verde Canyon Roots Gathering Music Summit & Recital Program needs a banner design to welco...

We are looking for a banner to use as a backdrop where people can take pictures and promote the event as they upload to social media. The music conference primarily targets high school students so we are looking for a design that will attract a younger audience. The festival revolves around music appreciation in the US/Mexico border. We like the "Mesa VerdeCanyon Roots Gathering" trumpet logo on the "5th annual" design attached, but we are open to other designs.
Target Market(s)
ages 15-45
Colors
Designer to choose colors to be used in the design.

```html
<!DOCTYPE html>
<html lang="en">
<head>
<meta charset="utf-8">
<title>Mesa Verde Canyon Roots Gathering – Music Summit &amp; Recital Program</title>
<link rel="stylesheet" href="https://fonts.googleapis.com/css2?family=Oswald:wght@400;700&family=Montserrat:wght@300&family=Roboto:wght@300;400;700&display=swap">
<style>
  :root {
    --bg-deep: #1e0a3c;
    --bg-mid: #321560;
    --bg-blue: #2a2a8a;
    --wave-magenta: #8a2fb8;
    --wave-violet: #5a3cc0;
    --title-white: #ffffff;
    --title-pink: #f3a8ff;
    --rule-peach: #f4a97a;
    --dot-grey: #8f8c9c;
    --eq-pink: #ff6fa8;
    --eq-cream: #f4e9b0;
    --eq-blue: #6a74e8;
  }
  * { margin: 0; padding: 0; box-sizing: border-box; }
  html, body { width: 1200px; height: 960px; overflow: hidden; background: var(--bg-deep); }
  .banner {
    position: relative;
    width: 1200px;
    height: 960px;
    overflow: hidden;
    background:
      radial-gradient(circle at 50% 40%, rgba(120,70,200,0.35) 0%, rgba(0,0,0,0) 40%),
      linear-gradient(135deg, var(--bg-mid) 0%, var(--bg-deep) 55%, var(--bg-blue) 100%);
  }
  .wave {
    position: absolute;
    border-radius: 50%;
    filter: blur(6px);
  }
  .wave--left {
    left: -180px; top: -120px; width: 620px; height: 900px;
    background: radial-gradient(ellipse at 40% 40%, rgba(138,47,184,0.75) 0%, rgba(138,47,184,0.25) 45%, rgba(0,0,0,0) 70%);
    transform: rotate(-20deg);
  }
  .wave--right {
    right: -160px; top: -140px; width: 560px; height: 760px;
    background: radial-gradient(ellipse at 55% 40%, rgba(90,60,192,0.75) 0%, rgba(90,60,192,0.25) 45%, rgba(0,0,0,0) 70%);
    transform: rotate(25deg);
  }
  .equalizer {
    position: absolute;
    left: 0; top: 690px; width: 1200px; height: 190px;
    background:
      linear-gradient(180deg, rgba(0,0,0,0) 0%, rgba(244,233,176,0.35) 35%, rgba(255,111,168,0.45) 50%, rgba(106,116,232,0.4) 65%, rgba(0,0,0,0) 100%);
    -webkit-mask: linear-gradient(90deg, transparent 0%, #000 6%, #000 94%, transparent 100%);
            mask: linear-gradient(90deg, transparent 0%, #000 6%, #000 94%, transparent 100%);
  }
  .baseline-rule {
    position: absolute; left: 0; top: 798px; width: 1200px; height: 2px;
    background: rgba(255,200,230,0.6);
  }
  .dots { position: absolute; display: flex; flex-direction: column; gap: 45px; }
  .dots span { display: block; width: 14px; height: 14px; border-radius: 50%; background: var(--dot-grey); }
  .dots--left { left: 70px; top: 44px; }
  .dots--right { left: 1134px; top: 580px; }
  .edition { position: absolute; left: 0; top: 0; }
  .edition text { font-family: 'Roboto', Arial, sans-serif; fill: var(--title-white); }
  .edition .edition__number { font-weight: 700; }
  .edition .edition__label { font-weight: 300; }
  .title {
    position: absolute; left: 298px; top: 196px;
    line-height: 1;
  }
  .title__top {
    display: block;
    font-family: 'Oswald', 'Arial Narrow', sans-serif;
    font-weight: 400;
    font-size: 112px;
    color: var(--title-white);
    letter-spacing: 0;
    white-space: nowrap;
  }
  .title__bottom {
    display: block;
    margin-top: 8px;
    font-family: 'Montserrat', Arial, sans-serif;
    font-weight: 300;
    font-size: 92px;
    color: var(--title-pink);
    white-space: nowrap;
  }
  .rule {
    position: absolute; left: 378px; top: 520px; width: 444px; height: 3px;
    background: var(--rule-peach);
  }
  .subtitle {
    position: absolute; left: 0; top: 568px; width: 1220px;
    text-align: center;
    font-family: 'Roboto', Arial, sans-serif;
    font-weight: 300;
    font-size: 35px;
    color: var(--title-white);
  }
</style>
</head>
<body>
  <div class="banner">
    <div class="wave wave--left" role="img" aria-label="Flowing magenta line-wave pattern"></div>
    <div class="wave wave--right" role="img" aria-label="Flowing violet line-wave pattern"></div>

    <div class="dots dots--left"><span></span><span></span><span></span><span></span><span></span><span></span></div>
    <div class="dots dots--right"><span></span><span></span><span></span><span></span><span></span><span></span></div>

    <svg class="edition" width="300" height="500" viewBox="0 0 300 500" aria-label="5th Annual">
      <g transform="translate(282,468) rotate(-90)">
        <text class="edition__number" x="0" y="-60" font-size="66" textLength="102" lengthAdjust="spacingAndGlyphs">5TH</text>
        <text class="edition__label" x="0" y="0" font-size="72" textLength="252" lengthAdjust="spacingAndGlyphs">ANNUAL</text>
      </g>
    </svg>

    <h1 class="title">
      <span class="title__top">Mesa VerdeCanyon</span>
      <span class="title__bottom">Roots Gathering</span>
    </h1>

    <div class="rule"></div>
    <p class="subtitle">Music Summit &amp; Recital Program</p>

    <div class="equalizer" role="img" aria-label="Glowing audio equalizer bars in cream, pink and blue"></div>
    <div class="baseline-rule"></div>
  </div>
</body>
</html>
```